In Home Senior Care Agency Business Card Design Needed

At Silver Birch Helpers, we don't just work in the care-giving industry. We truly care.

We are dedicated to providing personable, hands-on and integrated caring services that aim to help people maintain safe and comfortable life standards within the familiar settings of their own homes.

We would like to see designs that use my logo colors obviously. The final design will be modern, yet professional and semi-minimalistic. It should communicate an well-established company that is innovative. We would also like the design to have that 'flat' design look. Ideally having the design roll over to the backend of the card. Most likely it will be printed on a Matte paper with a die cut (either 2 rounded corners -leaf cut) or all rounded.

Target Market(s)

Baby boomer generation. 45 years and older.

Industry/Entity Type

Business

Contact Information for Business Card

Text for Front:
Slogan somewhere "Kind Hands. Warm Hearts. Home.”

Darren Holloway
President

Cell: 512.608.7719
Phone: 512.274.6051
E: Darren@silverbirchhelpers.net
W: www.SilverBirchHelpers.net

Back:
-Meal Preparation
-Transportation
-Light Housekeeping
-Bathing Assistance
-Companionship

Font styles to use
Serif
Sans Serif

Requirements
Must have
• Flat, modern, professional design. Not too many colors. Match my colors in logo. Design of card must reflect from the front onto the back. Evenly spaced font.
Nice to have
• Try to work off current logo scheme, but logo may need to be redesigned.
Should not have
• Not too many colors.

```html
<!DOCTYPE html>
<html lang="en">
<head>
<meta charset="utf-8">
<title>Silver Birch Helpers – Business Card</title>
<link rel="stylesheet" href="https://fonts.googleapis.com/css2?family=Cormorant+Garamond:ital,wght@0,500;1,500&family=Questrial&family=Open+Sans:wght@400;600;700&display=swap">
<style>
  :root {
    --backdrop: #1e1e1f;
    --paper: #f7f7f5;
    --green: #1d5a2e;
    --orange: #e8952a;
    --ink: #4a4a4a;
    --rule: #d6d6d2;
    --olive: #6c6026;
    --olive-dark: #5b501e;
    --band: #c8b87e;
    --band-ink: #544a1d;
    --pale-gold: #d9cb92;
  }
  * { margin: 0; padding: 0; box-sizing: border-box; }
  html, body { width: 1200px; height: 1000px; overflow: hidden; }
  body { background: var(--backdrop); position: relative; font-family: "Open Sans", Arial, sans-serif; }

  .card {
    position: absolute;
    left: 353px;
    width: 530px;
    height: 302px;
    border-radius: 16px;
    overflow: hidden;
  }

  /* Front */
  .card-front { top: 164px; background: var(--paper); }
  .front-brand {
    position: absolute;
    left: 28px; top: 122px;
    width: 200px;
    text-align: center;
  }
  .brand-name {
    font-family: "Cormorant Garamond", Georgia, serif;
    font-weight: 500;
    font-size: 34px;
    line-height: 30px;
    color: var(--green);
  }
  .slogan {
    margin-top: 8px;
    font-family: "Cormorant Garamond", Georgia, serif;
    font-style: italic;
    font-weight: 500;
    font-size: 15px;
    color: var(--green);
  }
  .divider {
    position: absolute;
    left: 237px; top: 92px;
    width: 1px; height: 118px;
    background: var(--rule);
  }
  .contact { position: absolute; left: 260px; top: 90px; }
  .person-name { font-weight: 700; font-size: 15.5px; color: var(--green); line-height: 20px; letter-spacing: 0.2px; }
  .person-title { font-size: 12.5px; color: var(--ink); line-height: 18px; letter-spacing: 0.3px; }
  .contact-list { list-style: none; margin-top: 15px; }
  .contact-list li { font-size: 13px; line-height: 16px; color: var(--ink); letter-spacing: 0.7px; }
  .contact-list .label { font-weight: 700; color: var(--orange); margin-right: 3px; letter-spacing: 0; }

  /* Back */
  .card-back {
    top: 549px;
    background: linear-gradient(180deg, var(--olive) 0%, var(--olive-dark) 100%);
  }
  .back-brand {
    position: absolute;
    left: 0; right: 0; top: 128px;
    text-align: center;
    font-family: "Cormorant Garamond", Georgia, serif;
    font-weight: 500;
    font-size: 34px;
    line-height: 30px;
    color: var(--pale-gold);
  }
  .services-band {
    position: absolute;
    left: 0; right: 0; top: 217px;
    height: 68px;
    background: var(--band);
    display: flex;
    flex-direction: column;
    justify-content: center;
    align-items: center;
    font-family: "Questrial", Arial, sans-serif;
    font-size: 15px;
    line-height: 24px;
    letter-spacing: 0.2px;
    color: var(--band-ink);
  }
</style>
</head>
<body>
  <section class="card card-front">
    <div class="front-brand">
      <div class="brand-name">Silver Birch<br>Helpers</div>
      <div class="slogan">Kind Hands. Warm Hearts. Home.</div>
    </div>
    <div class="divider"></div>
    <div class="contact">
      <div class="person-name">Darren Holloway</div>
      <div class="person-title">President</div>
      <ul class="contact-list">
        <li><span class="label">T:</span>512.274.6051</li>
        <li><span class="label">M:</span>512.608.7719</li>
        <li><span class="label">E:</span>darren@silverbirchhelpers.net</li>
        <li><span class="label">W:</span>www.SilverBirchHelpers.net</li>
      </ul>
    </div>
  </section>

  <section class="card card-back">
    <div class="back-brand">Silver Birch<br>Helpers</div>
    <div class="services-band">
      <div>Meal Preparation · Transportation · Light Housekeeping</div>
      <div>Bathing Assistance · Companionship</div>
    </div>
  </section>
</body>
</html>
```